Web Design Services Create a Similar website to my Competitor

We would like a similar website designed like our main competitor with all the features there website has and more. Also we would like to accept payments through our website and to rank quickly with seo based on our home page and other page use of high traffic keywords. this is the website we would like to have ours designed similar to https://www.festivalpaintbay.com. we will be providing the same services and more just at a different location. We would also like to know be able to easily make adjustments to the website when its time to edit it please thanks.

Basically I am looking to have have similar website built almost exactly the same but with my logo, and other personalized information to my company Orla Maskrade Beauty Lounge. I will need to send you model images and logo design idea but the body and user interface of my competitor https://www.festivalpaintbay.com will be exactly the same. I can be reached anytime to answer any questions you may have.
Updates

Hi Designers I would like to clarify some information Festival Paint Bay is my Competitor we are not affiliated. I would like my website to be designed similar to hers but please do not take any content from her website to put on mine I will be providing images to be posted on my website. Also please do not use any of her videos or ClipTube videos on my website to avoid any legal issues. Thanks for your understanding.

Target Market(s)

Make up Application Services For Events and Trinidad and Tobago Carnival

Industry/Entity Type

Beauty and Makeup Application and services

Coding

Coded - Design and coding required

Number of Pages Required

5+ page

Font styles to use
Sans Serif

Colors
E54698
E96AAD
F1A4CE
F9D9EA
FCEFF6
A7469A
B969AE
D3A5CF
EDDBEB
F8F0F9

Requirements
Must have
• Must be similar to my competitor, need a video section, testimonial and must be easily able to navigate to information sections and book now payment notifications running on all pages so customers can easily book there spot for 2026 carnival
Nice to have
• I am looking to have a similar website to https://www.festivalpaintbay.com created but make it as minimal and modern
Should not have
• Project can be coded if it makes it easier to create a similar look to my competitor just ask that updates can easily be made later on.

```html
<!DOCTYPE html>
<html lang="en">
<head>
<meta charset="utf-8">
<title>Orla Maskrade Beauty Lounge – Get Carnival-Ready with Orla Maskrade</title>
<link rel="stylesheet" href="https://fonts.googleapis.com/css2?family=Teko:wght@500;600&family=Plus+Jakarta+Sans:wght@400;500;600&family=Playfair+Display:ital,wght@1,400;1,600&display=swap">
<style>
:root{
  --navy:#2d2157;
  --magenta:#e2186c;
  --berry:#a7469a;
  --blush:#f9d5e4;
  --card:#f4f4f5;
  --ink:#2a2440;
  --muted:#6b6478;
  --white:#ffffff;
  --line:#b3a7c9;
}
*{box-sizing:border-box;margin:0;padding:0}
html,body{width:1200px;height:4155px;overflow:hidden}
body{position:relative;background:var(--white);font-family:"Plus Jakarta Sans",Arial,sans-serif;color:var(--ink)}
.heading{font-family:"Teko",Impact,sans-serif;font-weight:600;line-height:1;color:var(--navy);letter-spacing:.3px}
.accent{color:var(--magenta)}
.btn{position:absolute;display:flex;align-items:center;justify-content:center;border-radius:20px;font-family:"Playfair Display",Georgia,serif;font-style:italic;font-size:11px;color:var(--white);background:linear-gradient(90deg,var(--magenta),var(--navy));text-decoration:none;white-space:nowrap}
.btn.light{background:var(--white);color:var(--navy)}
.btn.outline{background:var(--magenta);border:1px solid var(--white)}

/* header */
.site-header{position:absolute;left:0;top:0;width:1200px;height:62px;background:var(--white)}
.brand{position:absolute;left:106px;top:12px;font-family:"Teko",sans-serif;font-weight:600;font-size:20px;line-height:.95;color:var(--navy);width:150px}
.brand .dot{display:inline-block;width:8px;height:8px;border-radius:50%;background:var(--magenta);margin-right:5px;vertical-align:2px}
.nav{position:absolute;top:23px;font-size:10px;font-weight:600;color:var(--ink)}
.nav.current{color:var(--magenta)}
.nav.current::after{content:"";position:absolute;left:50%;top:17px;width:8px;height:3px;margin-left:-4px;background:var(--magenta);border-radius:2px}

/* hero */
.hero{position:absolute;left:0;top:62px;width:1200px;height:562px;background:linear-gradient(90deg,#3a1a4f 0%,#8a2a6e 35%,#d8357e 55%,#e9458f 68%,#f08a3a 82%,#2f8ad0 100%)}
.hero-title{position:absolute;left:106px;top:156px;font-size:58px;color:var(--white)}
.hero-sub{position:absolute;left:106px;top:298px;width:440px;font-size:16px;line-height:1.35;color:var(--white)}

/* events */
.section-title{position:absolute;left:0;width:1200px;text-align:center;font-size:56px}
.event-card{position:absolute;top:794px;width:313px;height:330px;background:var(--card)}
.event-card .photo{height:217px}
.event-card .date{margin-top:20px;text-align:center;font-size:11px;color:var(--magenta)}
.event-card .name{margin-top:12px;text-align:center;font-size:16px;line-height:1.4;font-weight:500;color:var(--ink)}

/* comparison */
.compare{position:absolute;left:0;top:1261px;width:1200px;height:607px;background:var(--blush)}
.compare h3{font-size:30px}
.cons{list-style:none;font-size:13px;line-height:1.4;color:var(--ink)}
.cons li{margin-bottom:14px;padding-left:12px;text-indent:-12px}
.cons li::before{content:"X ";color:var(--magenta)}
.perks{list-style:none;font-size:13px;color:var(--ink)}
.perks li{height:30.6px;display:flex;align-items:flex-start;gap:10px}
.perks svg{flex:none;margin-top:2px}
.monogram{position:absolute;font-family:"Teko",sans-serif;font-weight:500;color:var(--navy);line-height:.9}

/* band */
.band{position:absolute;left:0;top:1868px;width:1200px;height:311px;background:linear-gradient(90deg,#2e2a62 0%,#7c2463 45%,#e2186c 100%)}

/* testimonial */
.quote{position:absolute;left:587px;top:2428px;width:400px;font-family:"Playfair Display",Georgia,serif;font-style:italic;font-size:17px;line-height:1.88;color:var(--ink)}
.arrow{position:absolute;top:2717px;width:34px;height:34px;border:1.5px solid var(--magenta);border-radius:50%;display:flex;align-items:center;justify-content:center}

/* products */
.product{position:absolute;top:3807px;width:181px;height:180px;border:1px solid #e2e2e6;background:var(--white);display:flex;align-items:center;justify-content:center}
.product .shot{width:140px;height:140px;border-radius:6px}
</style>
</head>
<body>

<header class="site-header">
  <div class="brand"><span class="dot"></span>Orla Maskrade Beauty Lounge</div>
  <a class="nav current" style="left:495px">Home</a>
  <a class="nav" style="left:553px">Glam Anywhere</a>
  <a class="nav" style="left:656px">Glam Store</a>
  <a class="nav" style="left:739px">Trinidad</a>
  <a class="nav" style="left:806px">Jamaica</a>
  <a class="nav" style="left:876px">More</a>
  <a class="btn" style="left:931px;top:16px;width:163px;height:31px">Choose Your Destination</a>
</header>

<section class="hero">
  <div role="img" aria-label="Smiling carnival masquerader with glitter mask and rainbow feather headdress" style="position:absolute;inset:0;background:radial-gradient(ellipse at 68% 45%,rgba(240,120,170,.55),transparent 60%)"></div>
  <h1 class="heading hero-title">Get Carnival-Ready<br>with Orla Maskrade</h1>
  <p class="hero-sub">Your All-In-One Carnival Beauty Concierge Because You Deserve a Stress-Free Start to the Road.</p>
  <a class="btn outline" style="left:106px;top:377px;width:163px;height:31px">Choose Your Destination</a>
</section>

<h2 class="heading section-title" style="top:700px">Upcoming <span class="accent">Events</span></h2>

<article class="event-card" style="left:106px">
  <div class="photo" role="img" aria-label="Masquerader in red and orange feathered headpiece" style="background:linear-gradient(135deg,#e0452a,#d9346f 50%,#2f5fb0)"></div>
  <p class="date">26 October 2025</p>
  <p class="name">Tobago - Orla Maskrade<br>Beauty Lounge</p>
</article>
<article class="event-card" style="left:444px">
  <div class="photo" role="img" aria-label="Carnival dancer in yellow and pink feathers against a grey wall" style="background:linear-gradient(135deg,#f2c733,#e2406f 45%,#9a9a9a)"></div>
  <p class="date">2 August 2025</p>
  <p class="name">Toronto Orla Maskrade<br>Beauty Lounge</p>
</article>
<article class="event-card" style="left:781px">
  <div class="photo" role="img" aria-label="Two masqueraders in colourful feathered costumes" style="background:linear-gradient(135deg,#f0b23a,#e04a86 45%,#3d6fc4)"></div>
  <p class="date">4 August 2025</p>
  <p class="name">Barbados - Orla Maskrade<br>Beauty Lounge</p>
</article>

<a class="btn" style="left:541px;top:1157px;width:117px;height:29px">View all Events</a>

<section class="compare">
  <h3 class="heading" style="position:absolute;left:200px;top:102px;width:330px">Without Orla Maskrade, your Carnival morning <span class="accent">might look</span> like this</h3>
  <ul class="cons" style="position:absolute;left:200px;top:232px;width:300px">
    <li>4am makeup appointment across town</li>
    <li>Ubering to a hairstylist who’s running late</li>
    <li>Trying to lace up a frontline costume alone</li>
    <li>Now you’re sweating out your beat before you hit the road</li>
  </ul>
  <div style="position:absolute;left:599px;top:75px;width:1px;height:330px;background:var(--line)"></div>
  <h3 class="heading" style="position:absolute;left:647px;top:80px;width:400px">With Orla Maskrade? <span class="accent">It’s a luxury prep</span> lounge, not a panic room.</h3>
  <p style="position:absolute;left:647px;top:168px;width:360px;font-size:9px;line-height:1.75;color:var(--ink)">Orla Maskrade is your go-to spot for polished Carnival makeup, hair and photos founded by pro MUA Rina Lustre since 2017. Every service is built to make you feel like royalty with all you need in one place:</p>
  <ul class="perks" style="position:absolute;left:647px;top:244px">
    <li><svg width="20" height="10" viewBox="0 0 20 10"><path d="M1 5l3 3 6-7M8 7l2 1 8-7" fill="none" stroke="#2d2157" stroke-width="1.4"/></svg>Pro Makeup</li>
    <li><svg width="20" height="10" viewBox="0 0 20 10"><path d="M1 5l3 3 6-7M8 7l2 1 8-7" fill="none" stroke="#2d2157" stroke-width="1.4"/></svg>Photoshoot</li>
    <li><svg width="20" height="10" viewBox="0 0 20 10"><path d="M1 5l3 3 6-7M8 7l2 1 8-7" fill="none" stroke="#2d2157" stroke-width="1.4"/></svg>Shuttle</li>
    <li><svg width="20" height="10" viewBox="0 0 20 10"><path d="M1 5l3 3 6-7M8 7l2 1 8-7" fill="none" stroke="#2d2157" stroke-width="1.4"/></svg>Seamstress</li>
    <li><svg width="20" height="10" viewBox="0 0 20 10"><path d="M1 5l3 3 6-7M8 7l2 1 8-7" fill="none" stroke="#2d2157" stroke-width="1.4"/></svg>Refreshments</li>
    <li><svg width="20" height="10" viewBox="0 0 20 10"><path d="M1 5l3 3 6-7M8 7l2 1 8-7" fill="none" stroke="#2d2157" stroke-width="1.4"/></svg>Bag Check</li>
  </ul>
  <ul class="perks" style="position:absolute;left:819px;top:244px">
    <li><svg width="20" height="10" viewBox="0 0 20 10"><path d="M1 5l3 3 6-7M8 7l2 1 8-7" fill="none" stroke="#2d2157" stroke-width="1.4"/></svg>Carnival Hair</li>
    <li><svg width="20" height="10" viewBox="0 0 20 10"><path d="M1 5l3 3 6-7M8 7l2 1 8-7" fill="none" stroke="#2d2157" stroke-width="1.4"/></svg>Reels</li>
    <li><svg width="20" height="10" viewBox="0 0 20 10"><path d="M1 5l3 3 6-7M8 7l2 1 8-7" fill="none" stroke="#2d2157" stroke-width="1.4"/></svg>Dressing Rooms</li>
    <li><svg width="20" height="10" viewBox="0 0 20 10"><path d="M1 5l3 3 6-7M8 7l2 1 8-7" fill="none" stroke="#2d2157" stroke-width="1.4"/></svg>Dressing Assistants</li>
    <li><svg width="20" height="10" viewBox="0 0 20 10"><path d="M1 5l3 3 6-7M8 7l2 1 8-7" fill="none" stroke="#2d2157" stroke-width="1.4"/></svg>Coffee &amp; Tea</li>
  </ul>
  <h3 class="heading" style="position:absolute;left:0;top:440px;width:1200px;text-align:center;font-size:36px">Don’t do this to yourself?</h3>
  <a class="btn" style="left:546px;top:497px;width:107px;height:30px">See Packages</a>
  <div class="monogram" style="left:52px;top:555px;font-size:20px">Orla<br>Maskrade</div>
</section>

<section class="band">
  <h2 class="heading" style="position:absolute;left:0;top:64px;width:1200px;text-align:center;font-size:58px;color:var(--white)">Comprehensive Carnival<br>Prep—Tailored Just for You.</h2>
  <a class="btn light" style="left:541px;top:216px;width:118px;height:29px">Yes, I Need This</a>
</section>

<h2 class="heading section-title" style="top:2254px">Real Stories from Our <span class="accent">Glam Fam.</span></h2>

<div style="position:absolute;left:213px;top:2355px;width:274px;height:410px;border:2px solid var(--magenta);border-left:0;border-bottom:0"></div>
<div role="img" aria-label="Masquerader in gold Venetian mask and feathered hat" style="position:absolute;left:200px;top:2368px;width:275px;height:406px;background:linear-gradient(160deg,#c9a06a,#6b4a35 55%,#3b2a24);border-radius:0 0 140px 140px / 0 0 120px 120px"></div>

<div style="position:absolute;left:587px;top:2388px;color:var(--magenta);font-size:17px;letter-spacing:4px">★★★★★</div>
<p class="quote">“ There are many variations of passages of lorem Ipsum available, but the majority have suffered alteration in some form, by injected humour, or randomised words which don’t look even slightly If you are going to use a passage of lorem ipsum. ”</p>
<p style="position:absolute;left:587px;top:2645px;font-size:17px;font-weight:500">Finibus Bonorum</p>
<p style="position:absolute;left:587px;top:2673px;font-size:9px;color:var(--ink)">Contrary to popular</p>
<div class="arrow" style="left:589px"><svg width="8" height="10" viewBox="0 0 8 10"><path d="M6 1L2 5l4 4" fill="none" stroke="#2a2440" stroke-width="1.5"/></svg></div>
<div class="arrow" style="left:632px"><svg width="8" height="10" viewBox="0 0 8 10"><path d="M2 1l4 4-4 4" fill="none" stroke="#2a2440" stroke-width="1.5"/></svg></div>

<section style="position:absolute;left:0;top:3065px;width:1200px;height:492px;background:var(--blush)"></section>
<div role="img" aria-label="Video of three masqueraders in blue and orange feathered costumes" style="position:absolute;left:200px;top:2849px;width:800px;height:405px;background:linear-gradient(90deg,#1c2a3a,#2c6a8a 30%,#c8623a 55%,#2c6a8a 75%,#1c2a3a)"></div>
<div style="position:absolute;left:570px;top:3022px;width:60px;height:60px;border-radius:50%;background:var(--magenta);display:flex;align-items:center;justify-content:center">
  <svg width="18" height="20" viewBox="0 0 18 20"><path d="M3 2l13 8-13 8z" fill="#fff"/></svg>
</div>

<h2 class="heading" style="position:absolute;left:200px;top:3302px;font-size:56px;white-space:nowrap">Orla Maskrade slots <span class="accent">disappear fast</span></h2>
<p style="position:absolute;left:200px;top:3380px;width:600px;font-size:16px;line-height:1.4">We book out every year. Don’t wait till “next time.” This is your moment. Secure your glam slot before they vanish.</p>
<a class="btn" style="left:200px;top:3450px;width:145px;height:31px">See Availability Now!</a>
<div class="monogram" style="left:940px;top:3380px;font-size:42px">Orla<br>Maskrade</div>

<h2 class="heading section-title" style="top:3630px">What You’ll <span class="accent">Need</span></h2>
<p style="position:absolute;left:265px;top:3714px;width:670px;text-align:center;font-size:12.5px;line-height:1.8;color:var(--ink)">Everything you forgot to pack—we’ve got you. from setting spray to sweat-proof lash glue, shop our carnival-ready essentials straight from Marketbay. curated by the Orla Maskrade team for masqueraders who need everything to stay in place from sunrise to the road.</p>

<div class="product" style="left:200px"><div class="shot" role="img" aria-label="Multi-pack of seamless underwear" style="background:linear-gradient(135deg,#f2d6cc,#8a6a78)"></div></div>
<div class="product" style="left:406px"><div class="shot" role="img" aria-label="Bottle of liquid foundation" style="background:linear-gradient(135deg,#ffffff,#7a4a34 60%,#ffffff)"></div></div>
<div class="product" style="left:613px"><div class="shot" role="img" aria-label="Gel shoe insoles pack" style="background:linear-gradient(135deg,#f1c640,#2f4ea0 50%,#e9e9ec)"></div></div>
<div class="product" style="left:819px"><div class="shot" role="img" aria-label="Stick deodorant" style="background:linear-gradient(135deg,#ffffff,#6f8a86 55%,#ffffff)"></div></div>

<a class="btn" style="left:538px;top:4021px;width:124px;height:29px">Shop on Marketbay</a>

</body>
</html>
```